Trailbend Depot Website - Sell Outdoor product

We are a mom and pop company that just opened our website.

We need a fresh, professional, and nice looking website for our outdoor products. We sell hunting, camping, fishing, and hiking products/accessories to name a few. Some of these products are optics, gun safes, gun bi-pods and tripods, gun lights, hunting camera, tents, hearing protection, targets, fishing poles, and hiking backpacks to name a few.

Our current website is: http://www.trailbenddepot.com . You'll see our logo on the website, and it is attached. We aren't married to this logo, so if the designer thinks they can modify it or even come up with a better design for the website, they are more than welcome to do so. We need someone with good images of their own (clip art and/or outdoor images) they can use if they need to for our website.

I also attached a idea I had in visio, but please don't think this is set in stone. It is just a very rough idea. You can also go to our marketvale site to see what we sell: www.marketvale.example/shops/q7rk482mzexn3d . Right now we sell everything on Marketvale, but our website will just focus on outdoor product. So please make it an outdoor focused website. And you can be creative with some of the product category names. We also want to leave room for some parallel product in the future. Like garden tools, back yard furniture, and BBQs.

Our company also wants to include a deals section on the website. We will probably update it once a week or month. I have included what I did for a deal and accompanying images for it. Image is called Morvelik (And the main images are 01 and 02).

We also want to make sure the file is compatible with our current web-hosting company, https://www.shelfnova.example. So I included a webpage layout zip folder. If you have any questions, please contact me.

This is for a PSD and HTML/CSS webpage. If you have any artwork or images that you own and want to use them for the webpage, please do so.

Target Market(s)

The hunter, outdoors person, camper, hiker, and etc.

Industry/Entity Type

It Company

Coding

Coded - Design and coding required

Number of Pages Required

3 page

Requirements
Must have
• The main page. PSD and HTML/CSS file.
• The category page. PSD and HTML/CSS file
• The product display page. PSD and HTML/CSS file
• Please also use some images that you have or from the sites below:
• You can get free stock images for 7 days (20 per day) from this site:
• https://www.pictovault.example/complimentary/PVXKRTZ/?utm_source=PVXKFreeRT&utm_medium=cpc&utm_campaign=PVXKFreeRT&gclid=QWLp8mdTzzRBHJuBbLpeW9nKpL
• Has 14 good sites:
• http://www.venturelog.example/article/519372
• Here are the ones I like:
• https://brightfram.example/
• http://quillorbit.example/
• http://www.pagedrift.example/free/nature
• http://www.stillbarrow.example/archive
• http://tinyglints.example/
• http://vel.prkwmd.example/search/hiking
• http://fetchlumo.blogspace.example/
• http://corvelpash.example/post/584920117463/download
• http://openpixelvault.example/
• If there is a photographer listed on or next to the image, on the bottom lower corner of the image, please put the photographer's name.
Nice to have
• I would like to have an unsubscribe page. If the designer has any of their own images of the outdoor world, and they want to use them, please do. Just make the right graphic changes to make it look good.
Should not have
• Try and keep green color to a minimum.

```html
<!DOCTYPE html>
<html lang="en">
<head>
<meta charset="utf-8">
<title>Trailbend Depot</title>
<link rel="stylesheet" href="https://fonts.googleapis.com/css2?family=Roboto:wght@400;500;700&family=Open+Sans:wght@400;600;700&display=swap">
<style>
:root{
  --dark:#333335;
  --darker:#2a2a2c;
  --light:#f1f1f1;
  --yellow:#ebb912;
  --orange:#ee6a1e;
  --text:#2b2b2b;
  --muted:#8a8a8a;
  --line:#d9d9d9;
  --white:#ffffff;
}
*{box-sizing:border-box;margin:0;padding:0}
html,body{width:1200px;height:3509px;overflow:hidden;background:var(--white)}
body{font-family:"Open Sans",Arial,sans-serif;color:var(--text);font-size:13px}
.canvas{position:relative;width:1200px;height:3509px;overflow:hidden}
.abs{position:absolute}
a{color:inherit;text-decoration:none}

/* header */
.topbar{left:0;top:0;width:1200px;height:98px;background:var(--light)}
.account{left:98px;top:14px;font-size:13px;color:var(--text)}
.account span{color:#c99a00}
.search{left:838px;top:8px;width:262px;height:34px;background:var(--white);border:1px solid #cfcfcf;display:flex;align-items:center;padding:0 12px;font-size:12px;color:#999;justify-content:space-between}
.headband{left:0;top:98px;width:1200px;height:50px}
.brand{left:440px;top:44px;width:320px;text-align:center;font-family:"Roboto",sans-serif;font-weight:700;font-size:34px;color:var(--darker);letter-spacing:.5px;display:flex;align-items:center;justify-content:center;gap:12px}
.brand i{display:inline-block;width:18px;height:18px;border-radius:50%;background:var(--yellow)}
.socials{left:96px;top:110px;display:flex;gap:18px}
.socials span{width:16px;height:16px;border-radius:50%;background:#d8d8d8;display:block}
.cart{left:995px;top:108px;display:flex;align-items:center;gap:8px;color:var(--white);font-size:12px}
.nav{left:0;top:168px;width:1200px;height:48px;border-top:1px solid var(--line);border-bottom:1px solid var(--line);display:flex;justify-content:space-between;align-items:center;padding:0 100px;font-size:11px;font-weight:700;letter-spacing:.2px}

/* hero */
.hero{left:0;top:218px;width:1200px;height:554px;background:radial-gradient(ellipse at 62% 45%,#b9824a 0%,#8a5a32 35%,#4d3422 75%,#2e2118 100%)}
.hero-title{left:100px;top:392px;font-family:"Roboto",sans-serif;font-weight:500;font-size:49px;line-height:61px;color:var(--orange)}
.hero-copy{left:100px;top:584px;width:650px;font-size:14px;line-height:22px;color:var(--white);font-weight:600}
.arrow{top:462px;font-size:60px;color:var(--white);font-family:"Roboto",sans-serif;line-height:1}
.dots{left:570px;top:748px;display:flex;gap:9px}
.dots span{width:10px;height:10px;border-radius:50%;background:rgba(255,255,255,.45)}
.dots span:first-child{background:rgba(255,255,255,.85)}

/* section headings */
.band{left:0;width:1200px}
.heading{left:0;width:1200px;text-align:center;font-family:"Roboto",sans-serif;font-size:37px;color:var(--text);line-height:1}
.heading em{font-style:normal;color:var(--yellow)}

.intro{left:98px;top:948px;width:1004px;font-size:13px;line-height:22px}
.rule{left:98px;top:1010px;width:1004px;height:2px;background:#cfcfcf}

/* deals */
.deals{left:0;top:1162px;width:1200px;height:405px;background:var(--light)}
.deal{top:1209px;width:229px;text-align:center}
.deal-photo{width:229px;height:172px;border:1px solid var(--line);box-shadow:0 1px 3px rgba(0,0,0,.15)}
.ph-detector{background:radial-gradient(ellipse at 50% 55%,#2f3f63 0%,#4c4c4c 22%,#a9a9a9 45%,#ffffff 70%)}
.ph-sight{background:radial-gradient(ellipse at 50% 50%,#262626 0%,#3f3f3f 28%,#9a9a9a 50%,#ffffff 72%)}
.ph-bag{background:radial-gradient(ellipse at 50% 50%,#1f1f1f 0%,#5a4030 30%,#c58a5a 45%,#ffffff 72%)}
.ph-telescope{background:radial-gradient(ellipse at 50% 45%,#1e1e1e 0%,#555 25%,#b5b5b5 48%,#ffffff 72%)}
.price{position:absolute;left:92px;top:150px;width:44px;height:44px;border-radius:50%;background:var(--yellow);color:var(--text);font-size:11px;font-weight:700;display:flex;align-items:center;justify-content:center}
.deal h3{margin-top:30px;font-size:13px;font-weight:600}
.deal .loc{font-size:10px;color:var(--muted);margin-top:4px}
.deal p{font-size:11px;line-height:15px;color:var(--muted);margin-top:5px}
.deal .more{display:block;font-size:11px;margin-top:8px}

/* testimonials */
.testi{left:0;top:1567px;width:1200px;height:480px;background:var(--yellow)}
.quote{left:0;top:1700px;width:1200px;text-align:center;font-family:"Roboto",sans-serif;font-weight:700;font-size:170px;color:var(--white);line-height:1;height:110px;overflow:hidden}
.testi-title{left:0;top:1812px;width:1200px;text-align:center;font-family:"Roboto",sans-serif;font-size:26px;color:var(--text)}
.testi-copy{left:150px;top:1856px;width:900px;text-align:center;font-size:12px;line-height:16px}
.btn-outline{left:541px;top:1946px;width:108px;height:42px;border:2px solid var(--text);display:flex;align-items:center;justify-content:center;font-size:12px;font-weight:600}

/* products */
.sidebar{left:96px;top:2224px;width:234px;height:478px;background:var(--light);border:1px solid var(--line)}
.side-head{height:47px;background:var(--yellow);color:var(--white);font-family:"Roboto",sans-serif;font-weight:700;font-size:15px;display:flex;align-items:center;padding-left:16px}
.side-list{list-style:none;padding:4px 0 0 0}
.side-list li{height:30.5px;display:flex;align-items:center;font-size:10px;color:#555;border-bottom:1px solid #e4e4e4}
.side-list li.folder{font-weight:700;font-size:9.5px;padding-left:22px;gap:12px}
.side-list li.folder::before{content:"";width:16px;height:11px;background:#6d6d6d;border-radius:1px}
.side-list li.sub{padding-left:38px}
.side-list li.sub::before{content:"•";margin-right:8px;color:#999}
.side-list li.deep{padding-left:62px}
.filter-title{left:98px;top:2785px;font-size:12px}
.slider{left:98px;top:2830px;width:232px;height:4px;background:#999}
.knob{top:2823px;width:16px;height:16px;border-radius:50%;background:var(--white);border:2px solid #777}
.filter-btn{left:98px;top:2849px;width:80px;height:34px;background:var(--yellow);color:var(--white);font-size:12px;font-weight:700;display:flex;align-items:center;justify-content:center}
.filter-range{left:190px;top:2858px;font-size:12px;color:#666}

.select{top:2222px;height:26px;border:1px solid #ccc;background:var(--white);font-size:9px;display:flex;align-items:center;padding:0 8px;color:#555}
.select b{color:var(--text);margin-left:3px}
.dropdown{left:818px;top:2248px;width:72px;background:var(--white);border:1px solid #ccc;box-shadow:0 2px 4px rgba(0,0,0,.12)}
.dropdown div{height:25px;font-size:9px;color:#555;display:flex;align-items:center;padding-left:8px;border-bottom:1px solid #eee}

.product{width:241px;height:349px;background:var(--white);border:1px solid var(--line);box-shadow:0 1px 3px rgba(0,0,0,.1)}
.prod-photo{position:absolute;left:14px;top:14px;width:211px;height:200px}
.ph-case{background:radial-gradient(ellipse at 50% 50%,#1a1a1a 0%,#2e2e2e 35%,#8c8c8c 55%,#ffffff 72%)}
.ph-light{background:radial-gradient(ellipse at 50% 50%,#3a3a3a 0%,#6e6e6e 25%,#c4c4c4 45%,#ffffff 65%)}
.ph-pack{background:radial-gradient(ellipse at 50% 50%,#1c1c1c 0%,#333 35%,#8f8f8f 52%,#ffffff 70%)}
.ph-rifle{background:radial-gradient(ellipse at 50% 50%,#1a1a1a 0%,#2f2f2f 25%,#9a9a9a 42%,#ffffff 62%)}
.ph-glasses{background:radial-gradient(ellipse at 50% 50%,#d87a2a 0%,#4a4a4a 30%,#a8a8a8 48%,#ffffff 66%)}
.prod-title{position:absolute;left:16px;top:240px;font-size:13px;font-weight:700}
.prod-price{position:absolute;left:16px;top:262px;font-size:19px;color:var(--yellow);font-weight:600}
.prod-price s{color:#777;font-size:13px;margin-right:8px}
.stars{position:absolute;right:16px;top:270px;font-size:11px;color:var(--yellow);letter-spacing:1px}
.prod-actions{position:absolute;left:0;bottom:0;width:100%;height:40px;border-top:1px solid #e5e5e5;display:flex;justify-content:space-between;align-items:center;padding:0 14px;font-size:11px}
.prod-actions span{display:flex;align-items:center;gap:6px}
.prod-actions .hot{color:var(--yellow)}

.pager{left:826px;top:3043px;display:flex;align-items:center;gap:4px;font-size:11px}
.pager .pg{width:16px;height:16px;border:1px solid #ccc;font-size:9px;display:flex;align-items:center;justify-content:center;color:#888}
.pager .pg.on{background:var(--yellow);border-color:var(--yellow);color:var(--white)}

/* footer */
.footer{left:0;top:3118px;width:1200px;height:320px;background:var(--dark);color:var(--white);text-align:center}
.footer h2{position:absolute;top:38px;left:0;width:1200px;font-family:"Roboto",sans-serif;font-weight:400;font-size:32px}
.footer .about{position:absolute;left:230px;top:98px;width:740px;font-size:14px;line-height:19px}
.footer .addr{position:absolute;top:168px;left:0;width:1200px;font-size:14px}
.footer .tel{position:absolute;top:192px;left:0;width:1200px;font-size:14px;word-spacing:2px}
.footer .tel span{margin-left:60px}
.btn-solid{position:absolute;left:489px;top:250px;width:222px;height:42px;background:var(--yellow);color:var(--white);font-size:14px;display:flex;align-items:center;justify-content:center;font-weight:600}
.bottombar{left:0;top:3438px;width:1200px;height:71px;background:var(--darker);border-top:3px solid #4a4a4a}
.copyright{left:98px;top:3468px;font-size:13px;color:var(--white)}
.foot-social{left:898px;top:3462px;display:flex;gap:26px}
.foot-social span{width:22px;height:22px;border-radius:50%;background:#cfcfcf;display:block}
</style>
</head>
<body>
<div class="canvas">

  <!-- header -->
  <div class="abs topbar"></div>
  <div class="abs account"><span>Sign in</span> &nbsp;or&nbsp; <span>Create an account</span></div>
  <div class="abs search">Search...
    <svg width="18" height="18" viewBox="0 0 18 18"><circle cx="7.5" cy="7.5" r="5.5" fill="none" stroke="#333" stroke-width="2"/><line x1="11.5" y1="11.5" x2="16.5" y2="16.5" stroke="#333" stroke-width="2.4"/></svg>
  </div>
  <svg class="abs headband" viewBox="0 0 1200 50" width="1200" height="50">
    <rect x="0" y="0" width="1200" height="47" fill="#333335"/>
  </svg>
  <svg class="abs" style="left:0;top:0" width="1200" height="156" viewBox="0 0 1200 156">
    <polygon points="400,0 800,0 800,98 770,150 430,150 400,98" fill="#ffffff"/>
    <polygon points="430,150 770,150 766,156 434,156" fill="#d5d5d5"/>
  </svg>
  <div class="abs brand"><i></i>Trailbend Depot</div>
  <div class="abs socials"><span></span><span></span><span></span><span></span></div>
  <div class="abs cart">
    <svg width="22" height="20" viewBox="0 0 22 20"><path d="M1 2h4l3 11h10l3-8H6.5" fill="none" stroke="#ffffff" stroke-width="1.8"/><circle cx="9" cy="17" r="1.8" fill="#fff"/><circle cx="17" cy="17" r="1.8" fill="#fff"/><circle cx="18" cy="3" r="3.5" fill="#ebb912"/></svg>
    ITEMS / $0.00
  </div>
  <nav class="abs nav">
    <a>BINOCULARS</a><a>METAL DETECTORS</a><a>MICROSCOPES</a><a>RIFLESCOPES</a><a>SAFE</a><a>SHOOTING ACCESSORIES</a><a>SPOTTING SCOPES</a><a>TELESCOPES</a>
  </nav>

  <!-- hero -->
  <div class="abs hero" role="img" aria-label="Photo of a tiger walking past a tree trunk in dry forest"></div>
  <div class="abs hero-title">Special<br>event needs<br>special effects!</div>
  <p class="abs hero-copy">Lorem ipsum dolor sit amet conse ctetur adipisicing elit, sed do eiusmod tempor incididunt ut labore et dolore magna aliqua. Ut enim ad minim veniam, quis nostrud exercitation ullamco laboris nisi ut aliquip ex ea commodo consequat. Duis aute irure dolo.</p>
  <div class="abs arrow" style="left:36px">&#10094;</div>
  <div class="abs arrow" style="left:1124px">&#10095;</div>
  <div class="abs dots"><span></span><span></span><span></span></div>

  <!-- welcome -->
  <svg class="abs band" style="top:870px" viewBox="0 0 1200 48" width="1200" height="48">
    <rect x="0" y="0" width="1200" height="48" fill="#333335"/>
    <polygon points="410,0 790,0 765,30 435,30" fill="#ffffff"/>
  </svg>
  <div class="abs heading" style="top:804px">Welcome To</div>
  <div class="abs heading" style="top:852px;color:var(--yellow)">Trailbend Depot</div>
  <p class="abs intro">Lorem ipsum dolor sit amet consectetur adipiscing elit. Praesent at lacus et augue mattis laoreet at in justo. Aliquam fermentum euismod alle vestibulum. Suspendisse tellus sapien auctor.</p>
  <div class="abs rule"></div>

  <!-- featured deals -->
  <svg class="abs band" style="top:1114px" viewBox="0 0 1200 48" width="1200" height="48">
    <rect x="0" y="0" width="1200" height="48" fill="#333335"/>
    <polygon points="410,0 790,0 760,34 440,34" fill="#ffffff"/>
  </svg>
  <div class="abs heading" style="top:1100px">Featured <em>Deals</em></div>
  <div class="abs deals"></div>

  <div class="abs deal" style="left:100px">
    <div class="deal-photo ph-detector" role="img" aria-label="Product photo of a metal detector"></div>
    <div class="price">$150</div>
    <h3>Claritas est etiam proces</h3>
    <div class="loc">Location: Thailand</div>
    <p>Claritas est etiam processynamicus, qui quitur mutationemconsuetudium lectorum irumtare quam littera gothica...</p>
    <a class="more">Read More</a>
  </div>
  <div class="abs deal" style="left:358px">
    <div class="deal-photo ph-sight" role="img" aria-label="Product photo of a red dot rifle sight"></div>
    <div class="price">$150</div>
    <h3>Claritas est etiam proces</h3>
    <div class="loc">Location: Thailand</div>
    <p>Claritas est etiam processynamicus, qui quitur mutationemconsuetudium lectorum irumtare quam littera gothica...</p>
    <a class="more">Read More</a>
  </div>
  <div class="abs deal" style="left:615px">
    <div class="deal-photo ph-bag" role="img" aria-label="Product photo of a shooting gear bag with targets"></div>
    <div class="price">$150</div>
    <h3>Claritas est etiam proces</h3>
    <div class="loc">Location: Thailand</div>
    <p>Claritas est etiam processynamicus, qui quitur mutationemconsuetudium lectorum irumtare quam littera gothica...</p>
    <a class="more">Read More</a>
  </div>
  <div class="abs deal" style="left:872px">
    <div class="deal-photo ph-telescope" role="img" aria-label="Product photo of a telescope on a tripod"></div>
    <div class="price">$150</div>
    <h3>Claritas est etiam proces</h3>
    <div class="loc">Location: Thailand</div>
    <p>Claritas est etiam processynamicus, qui quitur mutationemconsuetudium lectorum irumtare quam littera gothica...</p>
    <a class="more">Read More</a>
  </div>

  <!-- testimonials -->
  <div class="abs testi"></div>
  <svg class="abs band" style="top:1614px" viewBox="0 0 1200 58" width="1200" height="58">
    <rect x="0" y="0" width="1200" height="58" fill="#333335"/>
    <polygon points="410,0 790,0 760,38 440,38" fill="#ebb912"/>
  </svg>
  <div class="abs heading" style="top:1600px">Testimonials</div>
  <div class="abs quote">&ldquo;</div>
  <div class="abs testi-title">EU FUGIAT NULLA PARIATUR</div>
  <p class="abs testi-copy">Lorem ipsum dolor sit amet conse ctetur adipisicing elit, sed do eiusmod tempor incididunt ut labore et dolore magna aliqua. Ut enim ad minim veniam, quis nostrud exercitation ullamco laboris nisi ut aliquip ex ea commodo consequat. Duis aute irure dolor in reprehenderit in voluptate velit esse cillum dolore eu fugiat nulla pariatur. Excepteur sint occaecat cupidatat non proident.</p>
  <a class="abs btn-outline">SEE ALL</a>

  <!-- featured products -->
  <svg class="abs band" style="top:2092px" viewBox="0 0 1200 72" width="1200" height="72">
    <rect x="0" y="0" width="1200" height="72" fill="#333335"/>
    <polygon points="400,0 800,0 768,44 432,44" fill="#ffffff"/>
  </svg>
  <div class="abs heading" style="top:2102px">Featured <em>Products</em></div>

  <aside class="abs sidebar">
    <div class="side-head">CATAGORIES</div>
    <ul class="side-list">
      <li class="folder">USED F FOR CLOSED FOLDERS</li>
      <li class="folder">USED F FOR OPEN FOLDERS</li>
      <li class="sub">Lorem Ipsum Is Dummy</li>
      <li class="sub">Lorem Ipsum</li>
      <li class="deep">Just Like This</li>
      <li class="deep">Or Like This</li>
      <li class="sub">Lorem Ipsum Is Dummy Text</li>
      <li class="sub">Lorem</li>
      <li class="sub">Lorem Is Dummy Text</li>
      <li class="deep">Just Like This</li>
      <li class="deep">Or Like This</li>
      <li class="folder">USED F FOR CLOSED FOLDERS</li>
      <li class="folder">USED F FOR CLOSED FOLDERS</li>
      <li class="folder">USED F FOR CLOSED FOLDERS</li>
    </ul>
  </aside>
  <div class="abs filter-title">EZ Trieve Price Filters</div>
  <div class="abs slider"></div>
  <div class="abs knob" style="left:130px"></div>
  <div class="abs knob" style="left:308px"></div>
  <a class="abs filter-btn">FILTER</a>
  <div class="abs filter-range">Price: &nbsp;$25 - $85</div>

  <div class="abs select" style="left:818px;width:140px">Sort by <b>Default Order</b>&nbsp;&#9662;</div>
  <div class="abs select" style="left:966px;width:134px">Show <b>15 Products</b>&nbsp;&#9662;</div>

  <article class="abs product" style="left:356px;top:2283px">
    <div class="prod-photo ph-case" role="img" aria-label="Product photo of a black hard case"></div>
    <div class="prod-title">Product Title</div>
    <div class="prod-price"><s>$60</s>$85.00</div>
    <div class="stars">&#9733;&#9733;&#9733;&#9733;&#9734;</div>
    <div class="prod-actions"><span>&#128722; Add To Cart</span><span>&#9776; Details</span></div>
  </article>
  <article class="abs product" style="left:608px;top:2283px">
    <div class="prod-photo ph-light" role="img" aria-label="Product photo of a tactical flashlight"></div>
    <div class="prod-title">Another Product</div>
    <div class="prod-price">$30.00</div>
    <div class="prod-actions"><span>&#128722; Add To Cart</span><span>&#9776; Details</span></div>
  </article>
  <article class="abs product" style="left:861px;top:2283px">
    <div class="prod-photo ph-pack" role="img" aria-label="Product photo of a black hiking backpack"></div>
    <div class="prod-title">Yet Another Product</div>
    <div class="prod-price">$49.95</div>
    <div class="prod-actions"><span class="hot">&#128722; Add To Cart</span><span>&#9776; Details</span></div>
  </article>
  <article class="abs product" style="left:356px;top:2648px">
    <div class="prod-photo ph-rifle" role="img" aria-label="Product photo of a padded rifle case"></div>
    <div class="prod-title">Product Title</div>
    <div class="prod-price">$85.00</div>
    <div class="stars">&#9733;&#9733;&#9733;&#9733;&#9734;</div>
    <div class="prod-actions"><span>&#128722; Add To Cart</span><span>&#9776; Details</span></div>
  </article>
  <article class="abs product" style="left:608px;top:2648px">
    <div class="prod-photo ph-glasses" role="img" aria-label="Product photo of shooting sunglasses with orange lenses"></div>
    <div class="prod-title">Another Product</div>
    <div class="prod-price">$30.00</div>
    <div class="prod-actions"><span>&#128722; Add To Cart</span><span>&#9776; Details</span></div>
  </article>
  <article class="abs product" style="left:861px;top:2648px">
    <div class="prod-photo ph-pack" role="img" aria-label="Product photo of a black tactical backpack"></div>
    <div class="prod-title">Yet Another Product</div>
    <div class="prod-price">$49.95</div>
    <div class="prod-actions"><span>&#128722; Add To Cart</span><span>&#9776; Details</span></div>
  </article>

  <div class="abs dropdown">
    <div>Sort by Name</div><div>Sort by Price</div><div>Sort by Date</div><div>Sort by Rating</div>
  </div>

  <div class="abs pager">&lsaquo; Previous&nbsp;
    <span class="pg on">1</span><span class="pg">2</span><span class="pg">3</span><span class="pg">4</span><span class="pg">5</span><span class="pg">6</span>
    &nbsp;&nbsp;Next &rsaquo;
  </div>

  <!-- footer -->
  <footer class="abs footer">
    <h2>Contact Me</h2>
    <p class="about">Lorem ipsum dolor sit amet, consectetuer adipiscing elit. Praesent vestibulum m olestie lacus. Aenean nonummy hendrerit mauris. Phasellus porta. Fusce suscipit varius mi. Lorem ipsum dolor sit amet, consectetuer adipiscing elit. Praesent vestibulum molestie lacus. Morbi nunc odio, gravida at, cursus neca</p>
    <div class="addr">4418 - 4420 Alder Lane, Westbrook, KP14 72RD</div>
    <div class="tel">Telephone: +1 800 555 0147<span>E-mail: mail@trailbenddepot.example</span></div>
    <a class="btn-solid">DROP ME A MASSAGE</a>
  </footer>
  <div class="abs bottombar"></div>
  <div class="abs copyright">Copyright © 2015 - All Rights Reserved</div>
  <div class="abs foot-social"><span></span><span></span><span></span><span></span><span></span></div>

</div>
</body>
</html>
```